The Lantern Pact a non-fiction book on mindfulness COVER design needed

A non-fiction book about active mindfulness.
The Lantern Pact includes 21 different daily 'dares' which are action based activities to generate positive mindfulness - to become more contented with life.
Based on the teeaching of the New Thought movements of the early 20th century, think The Hollow, Climb and Gather Plenty.
The book is positive and uplifting. It fits into the self-help / spiritual / health segments. It skews female 40 to 50 year olds.
Think fresh colours like a bold orange or bright green.
What needs to be on the cover:
TITLE: The Lantern Pact
AUTHOR: Marcus Tindall
BLURB: Get clarity, focus, and a new zest for life by following The Lantern Pact for just 21 days.
Target Market(s)
Women 40-50 english speaking
Industry/Entity Type
Self-help / Health

```html
<!DOCTYPE html>
<html lang="en">
<head>
<meta charset="utf-8">
<title>The Lantern Pact – Book Cover</title>
<link href="https://fonts.googleapis.com/css2?family=Montserrat:wght@300;400;700;800;900&display=swap" rel="stylesheet">
<style>
  :root {
    --ink: #000000;
    --paper: #ffffff;
    --accent: #03ac8e;
    --art-light: #eceff0;
    --art-dark: #b9c2c4;
  }
  * { margin: 0; padding: 0; box-sizing: border-box; }
  html, body { width: 1200px; height: 758px; overflow: hidden; background: var(--paper); }
  body { font-family: 'Montserrat', sans-serif; color: var(--ink); }
  .cover { position: relative; width: 1200px; height: 758px; background: var(--paper); overflow: hidden; }

  /* Back cover */
  .back-title { position: absolute; left: 52px; top: 79px; font-weight: 900; line-height: 1; letter-spacing: -1px; }
  .back-title .title-small { display: block; font-size: 47px; }
  .back-title .title-large { display: block; font-size: 90px; margin-top: -11px; letter-spacing: -2px; }
  .back-copy { position: absolute; left: 54px; top: 222px; font-size: 22px; line-height: 27.3px; font-weight: 400; letter-spacing: 0.6px; }
  .back-copy strong { font-weight: 700; }
  .back-quote { position: absolute; left: 44px; top: 682px; font-size: 14.5px; font-weight: 700; color: var(--accent); white-space: nowrap; }
  .back-band { position: absolute; left: 51px; top: 708px; width: 304px; height: 50px; background: var(--accent); color: var(--paper); font-weight: 700; font-size: 15px; display: flex; align-items: center; justify-content: center; padding-bottom: 4px; }

  /* Spine */
  .spine-title, .spine-author { position: absolute; writing-mode: vertical-rl; white-space: nowrap; line-height: 1; }
  .spine-title { left: 580px; top: 52px; font-size: 30px; font-weight: 900; letter-spacing: 0.5px; }
  .spine-rule { position: absolute; left: 581px; top: 419px; width: 42px; height: 2px; background: var(--ink); }
  .spine-author { left: 585px; top: 440px; font-size: 31px; font-weight: 300; letter-spacing: 1px; }

  /* Front cover */
  .front-title { position: absolute; left: 688px; top: 40px; font-weight: 900; line-height: 1; }
  .front-title .title-small { display: block; font-size: 64px; letter-spacing: -1px; }
  .front-title .title-large { display: block; font-size: 170px; letter-spacing: -5px; margin-top: -14px; margin-left: -6px; }
  .front-art { position: absolute; left: 690px; top: 320px; width: 458px; height: 142px; background: linear-gradient(90deg, var(--art-light), var(--art-dark) 50%, var(--art-light)); }
  .front-blurb { position: absolute; left: 688px; width: 460px; top: 500px; text-align: center; font-size: 14.5px; font-weight: 800; line-height: 21.7px; }
  .front-blurb .highlight { color: var(--accent); }
  .front-blurb .big-number { font-size: 22px; }
  .front-author { position: absolute; left: 688px; width: 460px; top: 622px; text-align: center; font-size: 48px; font-weight: 300; line-height: 45px; }
</style>
</head>
<body>
<main class="cover">
  <section class="back-cover">
    <h2 class="back-title"><span class="title-small">THE LANTERN</span><span class="title-large">PACT</span></h2>
    <p class="back-copy"><strong>Lorem</strong> ipsum Lorem ipsum<br>Lorem ipsum Lorem ipsum<br>Lorem ipsum Lorem ipsum<br>Lorem ipsum Lorem ipsum<br>Lorem ipsum Lorem ipsum<br>Lorem ipsum Lorem ipsum<br>Lorem ipsum Lorem ipsum<br>Lorem ipsum Lorem ipsum<br>Lorem ipsum Lorem ipsum<br>Lorem ipsum Lorem ipsum<br>Lorem ipsum Lorem ipsum<br>Lorem ipsum Lorem ipsum .</p>
    <p class="back-quote">“Lorem ipsum Lorem ipsum Lorem ipsum”</p>
    <div class="back-band">LOREM IPSUM</div>
  </section>

  <section class="spine">
    <span class="spine-title">THE LANTERN PACT</span>
    <span class="spine-rule"></span>
    <span class="spine-author">MARCUS TINDALL</span>
  </section>

  <section class="front-cover">
    <h1 class="front-title"><span class="title-small">THE LANTERN</span><span class="title-large">PACT</span></h1>
    <div class="front-art" role="img" aria-label="Illustration of a pair of striking eyes with dark brows and lashes and green irises"></div>
    <p class="front-blurb">GET CLARITY<br>FOCUS, AND A NEW<br>ZEST FOR LIFE BY FOLLOWING<br><span class="highlight">THE LANTERN PACT</span> FOR JUST <span class="big-number">21</span> DAYS.</p>
    <p class="front-author">MARCUS<br>TINDALL</p>
  </section>
</main>
</body>
</html>
```